Online Marketing Agency Website

We are an online marketing agency that specializes in search marketing (SEM) for businesses of all sizes. Our core services include local search marketing, seo, paid search, paid social, graphic design, video production/editing and website design. We have an existing website that we launched a number of years ago but it's very outdated and we're currently too busy to design a new version.

Target Market(s)

Any business that needs online marketing services with an emphasis on search marketing.

Industry/Entity Type

Ad Agency

Number of Pages Required

4 page

Font styles to use
Sans Serif

Requirements
Must have
• Home page, interior page, blog page, contact us page.
Look and feel should be modern and clean and easy to navigate.
Sections for call outs for specific services: Business Marketing Strategy, Content Creation and Marketing, Graphic & Publication Design, Pay Per Click (PPC) Management, Search Engine Optimization, Social Media Management, Video Production & Editing, Website Hosting & Management, Website Design & Development
Use color from logo that was uploaded.

```html
<!DOCTYPE html>
<html lang="en">
<head>
<meta charset="utf-8">
<title>Apex Reach – Online Marketing. Elevated</title>
<link href="https://fonts.googleapis.com/css2?family=Questrial&family=Montserrat:wght@400;500;600&display=swap" rel="stylesheet">
<style>
:root{
  --orange:#ff4f17;
  --orange-soft:#ff8a63;
  --ink:#1b1b1b;
  --muted:#7a7a7a;
  --blush:#fdf1ec;
  --line:#e3e3e3;
  --footer:#1f2024;
  --footer-text:#cfcfcf;
  --white:#fff;
}
*{margin:0;padding:0;box-sizing:border-box}
html,body{width:1200px;height:4431px;overflow:hidden}
body{position:relative;background:var(--white);font-family:"Montserrat",sans-serif;color:var(--ink)}
.abs{position:absolute}
.head{font-family:"Questrial",sans-serif}
.accent{color:var(--orange)}
.btn{position:absolute;display:flex;align-items:center;justify-content:center;gap:10px;background:var(--orange);color:var(--white);font-weight:600;font-size:15px;border-radius:4px;text-transform:uppercase;white-space:nowrap}
.photo{position:absolute}

/* hero */
.hero{position:absolute;left:0;top:0;width:1200px;height:712px;background:var(--blush)}
.hero-photo{left:683px;top:0;width:517px;height:712px;background:linear-gradient(160deg,#5a4c44,#b7aca3 55%,#e9e3dd)}
.brand{position:absolute;display:flex;align-items:center;gap:10px}
.brand-mark{width:20px;height:20px;background:var(--orange)}
.brand-name{font-family:"Questrial",sans-serif;font-size:15px;color:var(--ink);letter-spacing:.5px}
.brand-tag{font-size:8px;color:var(--muted)}
.nav a{position:absolute;top:40px;font-size:11px;font-weight:500;color:var(--ink);text-decoration:none;text-transform:uppercase;white-space:nowrap}
.nav a.active{color:var(--orange);border-bottom:2px solid var(--orange);padding-bottom:6px}
.hero-kicker{left:162px;top:238px;font-size:14px;font-weight:600;color:var(--orange)}
.hero-title{left:160px;top:262px;font-size:60px;line-height:62px;font-weight:400}
.hero-sub{left:163px;top:460px;font-size:15px;line-height:25px;color:#333}

/* services */
.section-title{left:0;width:1200px;text-align:center;font-size:31px;line-height:37px}
.section-lede{left:340px;width:520px;text-align:center;font-size:12px;line-height:21px;color:var(--muted)}
.card{position:absolute;top:972px;width:203px;height:254px;text-align:center}
.card.is-active{background:var(--white);box-shadow:0 4px 16px rgba(0,0,0,.08);border-bottom:4px solid var(--orange)}
.card svg{margin-top:35px}
.card h3{font-family:"Questrial",sans-serif;font-weight:400;font-size:16px;line-height:22px;margin-top:20px;padding:0 20px}
.card p{font-size:10px;line-height:18px;color:var(--muted);margin-top:10px;padding:0 22px}
.dots{left:570px;top:1277px;display:flex;gap:10px}
.dots span{width:13px;height:13px;border-radius:50%;background:var(--ink)}
.dots span.on{background:none;border:3px solid var(--orange)}

/* about */
.about-band{left:0;top:1445px;width:1200px;height:487px;background:var(--blush)}
.about-photo{left:0;top:1369px;width:541px;height:489px;border-top-right-radius:60px;background:linear-gradient(140deg,#3a3430,#8d7a66 50%,#c9b59b)}
.about-kicker{left:650px;top:1536px;font-size:16px;font-weight:600}
.about-title{left:648px;top:1562px;font-size:35px}
.about-copy{left:650px;top:1630px;width:340px;font-size:11.5px;line-height:21px;color:var(--muted)}

/* video */
.video-kicker{left:174px;top:2010px;font-size:17px;font-weight:600}
.video-title{left:175px;top:2040px;font-size:29px;line-height:35px}
.video-photo{left:258px;top:2172px;width:464px;height:300px;border-radius:6px;background:linear-gradient(135deg,#2b2b2b,#7b7e80 50%,#cfd1d2)}
.video-note{left:396px;top:2400px;width:447px;height:120px;background:var(--white);padding:22px 20px 0 24px;font-size:11.5px;line-height:22px;color:var(--muted)}
.video-next{left:849px;top:2452px;width:40px;height:40px;border-radius:50%;background:var(--orange);display:flex;align-items:center;justify-content:center}
.topic-list{left:817px;top:2022px;list-style:none;font-size:14px}
.topic-list li{height:38px}
.topic-list li.on{color:var(--orange)}
.topic-list li.on span{border-bottom:1.5px solid var(--orange);padding:0 34px 6px 0}

/* cta */
.cta{left:0;top:2597px;width:1200px;height:353px;background:var(--orange)}
.cta-photo{left:232px;top:2632px;width:318px;height:275px;border-radius:50% 50% 40% 40%;background:linear-gradient(160deg,#f2ede7,#6c88b0 65%,#3e5b86)}
.cta-title{left:580px;top:2680px;font-size:29px;line-height:38px;color:var(--white)}
.cta-phone{left:581px;top:2812px;width:165px;height:40px;background:#1f1f1f;border-radius:4px;color:var(--white);display:flex;align-items:center;justify-content:center;gap:10px;font-size:15px}

/* blog */
.blog{left:0;top:2950px;width:1200px;height:628px;background:var(--blush)}
.blog-title{left:244px;top:3030px;font-size:34px}
.blog-arrow{top:3031px;width:36px;height:36px;border-radius:50%;display:flex;align-items:center;justify-content:center}
.post{position:absolute;top:3122px;width:262px}
.post-img{height:206px;position:relative}
.post-date{position:absolute;left:0;bottom:0;background:var(--orange);color:var(--white);font-size:11px;padding:6px 15px}
.post h3{font-family:"Questrial",sans-serif;font-weight:400;font-size:16px;line-height:21px;margin-top:24px;width:240px}
.post p{font-size:10.5px;line-height:21px;color:var(--muted);margin-top:8px}

/* contact */
.contact-kicker{left:162px;top:3610px;font-size:17px;font-weight:600}
.contact-title{left:160px;top:3640px;font-size:36px;color:var(--orange)}
.contact-copy{left:162px;top:3690px;width:330px;font-size:11.5px;line-height:21px;color:var(--muted)}
.contact-line{left:162px;display:flex;align-items:center;gap:14px;font-size:12px;color:var(--orange);text-decoration:underline}
.field{position:absolute;border-bottom:1px solid var(--line);font-size:10px;color:#aaa;padding-bottom:12px;height:34px}
.field.focus{border-bottom:2px solid var(--orange-soft);color:var(--ink)}

/* footer */
.footer{left:0;top:4054px;width:1200px;height:377px;background:var(--footer)}
.foot-head{font-size:12px;color:var(--orange);text-transform:uppercase}
.foot-list{list-style:none;font-size:10.5px;line-height:22.6px;color:var(--footer-text)}
.foot-list li::before{content:"";display:inline-block;width:4px;height:4px;border-radius:50%;background:var(--orange);margin-right:14px;vertical-align:middle}
.foot-contact{display:flex;gap:18px;font-size:10.5px;color:var(--footer-text)}
.social{top:4220px;width:33px;height:33px;border-radius:50%}
.copyright{left:0;top:4398px;width:1200px;text-align:center;font-size:10px;color:#bbb}
</style>
</head>
<body>

<!-- hero -->
<section class="hero">
  <div class="photo hero-photo" role="img" aria-label="Photo of a person working on a laptop"></div>
  <div class="brand" style="left:160px;top:24px">
    <span class="brand-mark"></span>
    <div><div class="brand-name">APEX REACH</div><div class="brand-tag">Online Marketing. Elevated</div></div>
  </div>
  <nav class="nav">
    <a class="active" href="#" style="left:574px">Home</a>
    <a href="#" style="left:629px">About</a>
    <a href="#" style="left:690px">Interior</a>
    <a href="#" style="left:762px">Blog</a>
    <a href="#" style="left:814px">Contact</a>
  </nav>
  <div class="btn" style="left:889px;top:29px;width:150px;height:36px;font-weight:500;text-transform:none">
    <svg width="14" height="14" viewBox="0 0 24 24"><path d="M6.6 10.8a15 15 0 0 0 6.6 6.6l2.2-2.2a1 1 0 0 1 1-.25 11 11 0 0 0 3.6.6 1 1 0 0 1 1 1V20a1 1 0 0 1-1 1A17 17 0 0 1 3 4a1 1 0 0 1 1-1h3.5a1 1 0 0 1 1 1 11 11 0 0 0 .6 3.6 1 1 0 0 1-.25 1z" fill="#fff"/></svg>
    555 010 2040
  </div>
  <div class="abs hero-kicker">APEX REACH</div>
  <h1 class="abs head hero-title">Online<br>Marketing.<br>Elevated</h1>
  <p class="abs hero-sub">Apex Reach Is A Full-Service Online<br>Marketing Agency</p>
  <div class="btn" style="left:162px;top:525px;width:210px;height:39px;font-size:14px">Get Started With Us</div>
</section>

<!-- services -->
<h2 class="abs head section-title" style="top:786px">Apex Reach is a Full-Service<br>Online <span class="accent">Marketing Agency.</span></h2>
<p class="abs section-lede" style="top:875px">We can handle any element of your online marketing so you can get back to doing what you do best — growing your business. All of our services are offered on an ‘a la carte’ basis.</p>

<div class="card is-active" style="left:172px">
  <svg width="64" height="56" viewBox="0 0 64 56" fill="none" stroke="#222" stroke-width="2"><rect x="6" y="4" width="52" height="38" rx="2"/><path d="M2 46h60M14 14l6 6M20 14l-6 6M44 28l6 6M50 28l-6 6"/><path d="M20 24c6 8 14 10 24 4" stroke="#ff4f17" stroke-dasharray="3 3"/></svg>
  <h3>Business Marketing Strategy.</h3>
  <p>Let us strategize the big picture for you. With decades of experience...</p>
</div>
<div class="card" style="left:388px">
  <svg width="64" height="56" viewBox="0 0 64 56" fill="none" stroke="#222" stroke-width="2"><rect x="8" y="4" width="48" height="36" rx="2"/><circle cx="34" cy="22" r="9" stroke="#ff4f17"/><path d="M31 18l6 4-6 4z"/><path d="M24 40v8h16v-8M18 52h28"/></svg>
  <h3>Content Creation and Marketing</h3>
  <p>You’ve heard it before. “Content is king.” Search engines love it and potential...</p>
</div>
<div class="card" style="left:607px">
  <svg width="64" height="56" viewBox="0 0 64 56" fill="none" stroke="#222" stroke-width="2"><path d="M32 6v10M22 16h20l-4 18H26z"/><circle cx="32" cy="24" r="3" stroke="#ff4f17"/><path d="M26 34l6 16 6-16M28 6h8"/></svg>
  <h3>Graphic &amp; Publication Design</h3>
  <p>Our designers have decades of experience in everything from tradeshow...</p>
</div>
<div class="card" style="left:823px">
  <svg width="64" height="56" viewBox="0 0 64 56" fill="none" stroke="#222" stroke-width="2"><rect x="20" y="2" width="24" height="46" rx="3"/><path d="M29 44h6"/><path d="M32 18v18l-4-3M32 18a3 3 0 0 1 6 0v12" stroke="#ff4f17"/></svg>
  <h3>Pay Per Click (PPC) Management</h3>
  <p>PPC advertising delivers some of the best ROI online...but it can be overwhelming...</p>
</div>
<div class="abs dots"><span class="on"></span><span></span><span></span></div>

<!-- about -->
<div class="abs about-band"></div>
<div class="photo about-photo" role="img" aria-label="Photo of a desk with two monitors and a keyboard"></div>
<div class="abs about-kicker">Welcome To</div>
<h2 class="abs head about-title">APEX <span class="accent">REACH</span></h2>
<p class="abs about-copy">Lorem Ipsum is simply dummy text of the printing and typesetting industry. Lorem Ipsum has been the industry's standard dummy text ever since the 1500s, when an unknown printer took a galley of type and scrambled it to make a type specimen book. It has survived not only five centuries, but also the leap into electronic typesetting, remaining essentially unchanged.</p>
<div class="btn" style="left:652px;top:1794px;width:143px;height:41px;font-size:14px;font-weight:500">Learn More</div>

<!-- video -->
<div class="abs video-kicker">The Growing Power of Video</div>
<h2 class="abs head video-title">Why Professional Video<br>Production and Editing Is<br>Necessary</h2>
<div class="photo video-photo" role="img" aria-label="Photo of a camera lens, phone and laptop"></div>
<p class="abs video-note">Yet, this doesn’t mean any type of video will generate results. The video has to be made professionally and look appealing and engaging. Research shows over 60% of online visitors are unlikely to trust a brand if they publish a poor quality video.</p>
<div class="abs video-next"><svg width="14" height="14" viewBox="0 0 14 14"><path d="M5 2l5 5-5 5" stroke="#fff" stroke-width="2" fill="none"/></svg></div>
<ul class="abs topic-list">
  <li>Paid Social</li><li>Paid Search</li><li>Graphic Design</li><li class="on"><span>Video Production/editing</span></li><li>Website Design</li>
</ul>

<!-- cta -->
<section class="abs cta"></section>
<div class="photo cta-photo" role="img" aria-label="Photo of a man seated, using a tablet"></div>
<h2 class="abs head cta-title">If you Have an any<br>Question for Contact us<br>Today !</h2>
<div class="abs cta-phone">
  <svg width="14" height="14" viewBox="0 0 24 24"><path d="M6.6 10.8a15 15 0 0 0 6.6 6.6l2.2-2.2a1 1 0 0 1 1-.25 11 11 0 0 0 3.6.6 1 1 0 0 1 1 1V20a1 1 0 0 1-1 1A17 17 0 0 1 3 4a1 1 0 0 1 1-1h3.5a1 1 0 0 1 1 1 11 11 0 0 0 .6 3.6 1 1 0 0 1-.25 1z" fill="#fff"/></svg>
  555 010 2040
</div>

<!-- blog -->
<section class="abs blog"></section>
<h2 class="abs head blog-title">BLOG <span class="accent">POST</span></h2>
<div class="abs blog-arrow" style="left:947px;background:#333"><svg width="12" height="12" viewBox="0 0 12 12"><path d="M8 2L4 6l4 4" stroke="#fff" stroke-width="2" fill="none"/></svg></div>
<div class="abs blog-arrow" style="left:993px;background:var(--orange)"><svg width="12" height="12" viewBox="0 0 12 12"><path d="M4 2l4 4-4 4" stroke="#fff" stroke-width="2" fill="none"/></svg></div>

<article class="post" style="left:301px">
  <div class="post-img" role="img" aria-label="Photo of a notebook with wireframe sketches" style="background:linear-gradient(135deg,#f1f1f1,#c9bfb5 60%,#8a5a3e)"><span class="post-date">23 july 2020</span></div>
  <h3>Lorem Ipsum is simply dummy text of the printing &amp; Type</h3>
  <p>Lorem Ipsum is simply dummy text of the printing and typesetting industry. Lorem Ipsum has been the industry's standard.</p>
</article>
<article class="post" style="left:593px">
  <div class="post-img" role="img" aria-label="Photo of a tablet showing analytics charts" style="background:linear-gradient(135deg,#d8d4cc,#5d5d5d 55%,#2e3a48)"><span class="post-date">23 july 2020</span></div>
  <h3>Lorem Ipsum is simply dummy text of the printing &amp; Type</h3>
  <p>Lorem Ipsum is simply dummy text of the printing and typesetting industry. Lorem Ipsum has been the industry's standard.</p>
</article>
<article class="post" style="left:886px">
  <div class="post-img" role="img" aria-label="Photo of a geometric wire sculpture on yellow" style="background:linear-gradient(135deg,#fff200,#e8d700 60%,#8f8a2a)"><span class="post-date">23 july 2020</span></div>
  <h3>Lorem Ipsum is simply dummy text of the printing &amp; Type</h3>
  <p>Lorem Ipsum is simply dummy text of the printing and typesetting industry. Lorem Ipsum has been the industry's standard.</p>
</article>
<article class="post" style="left:1178px">
  <div class="post-img" role="img" aria-label="Photo for a blog post" style="background:linear-gradient(135deg,#cfd6de,#4a5560)"><span class="post-date">23 july 2020</span></div>
  <h3>Lorem Ipsum is simply dummy text of the printing &amp; Type</h3>
  <p>Lorem Ipsum is simply dummy text of the printing and typesetting industry.</p>
</article>

<!-- contact -->
<div class="abs contact-kicker">Contact Us</div>
<h2 class="abs head contact-title">LET'S TALK</h2>
<p class="abs contact-copy">If you need a website, some SEO, paid social, graphic design, video production &amp; website design? Drop us aline we'd love to hear from you.</p>
<div class="abs contact-line" style="top:3776px">
  <svg width="14" height="14" viewBox="0 0 24 24"><path d="M6.6 10.8a15 15 0 0 0 6.6 6.6l2.2-2.2a1 1 0 0 1 1-.25 11 11 0 0 0 3.6.6 1 1 0 0 1 1 1V20a1 1 0 0 1-1 1A17 17 0 0 1 3 4a1 1 0 0 1 1-1h3.5a1 1 0 0 1 1 1 11 11 0 0 0 .6 3.6 1 1 0 0 1-.25 1z" fill="#ff4f17"/></svg>
  (+1) 555 010 2040
</div>
<div class="abs contact-line" style="top:3807px">
  <svg width="14" height="12" viewBox="0 0 14 12"><rect width="14" height="12" rx="1" fill="#ff4f17"/><path d="M1 2l6 4 6-4" stroke="#fff" stroke-width="1.3" fill="none"/></svg>
  hello@apexreach.example
</div>

<div class="field focus" style="left:543px;top:3692px;width:219px">Enter Name *</div>
<div class="field" style="left:784px;top:3692px;width:219px">Select Services</div>
<div class="field" style="left:543px;top:3766px;width:219px">Enter Phone *</div>
<div class="field" style="left:784px;top:3766px;width:219px">Enter Email *</div>
<div class="field" style="left:543px;top:3828px;width:460px;height:85px">Message *</div>
<div class="btn" style="left:829px;top:3939px;width:165px;height:38px;font-size:14px;font-weight:500">Send Message</div>

<!-- footer -->
<footer class="abs footer"></footer>
<div class="brand" style="left:198px;top:4150px;flex-direction:column;align-items:center;gap:8px">
  <span class="brand-mark"></span>
  <div style="text-align:center"><div class="brand-name" style="color:#8a8a8a">APEX REACH</div><div class="brand-tag">Online Marketing. Elevated</div></div>
</div>
<span class="abs social" style="left:183px;background:#3b5998"></span>
<span class="abs social" style="left:222px;background:#d7263d"></span>
<span class="abs social" style="left:262px;background:#1da1f2"></span>
<span class="abs social" style="left:303px;background:#5b7fb8"></span>

<div class="abs foot-head" style="left:387px;top:4100px">Sitemap</div>
<ul class="abs foot-list" style="left:387px;top:4138px"><li>Home</li><li>About</li><li>Services</li><li>Testimonials</li><li>Contact Us</li></ul>

<div class="abs foot-head" style="left:612px;top:4100px">Services</div>
<ul class="abs foot-list" style="left:612px;top:4138px"><li>Business Marketing Strategy</li><li>Content Creation And Marketing</li><li>Graphic &amp; Publication Design</li><li>Pay Per Click Management</li><li>Search Engine Optimization</li><li>Social Media Management</li><li>Video Production &amp; Editing</li><li>Website Hosting &amp; Management</li><li>Website Design &amp; Development</li></ul>

<div class="abs foot-head" style="left:838px;top:4100px">Contact Us</div>
<div class="abs foot-contact" style="left:838px;top:4140px;line-height:16px">
  <svg width="14" height="18" viewBox="0 0 14 18"><path d="M7 0a7 7 0 0 0-7 7c0 5 7 11 7 11s7-6 7-11a7 7 0 0 0-7-7z" fill="#ff4f17"/><circle cx="7" cy="7" r="2.5" fill="#1f2024"/></svg>
  <span>APEX REACH<br>101 - lorem ipsum simple<br>text print</span>
</div>
<div class="abs foot-contact" style="left:838px;top:4206px;align-items:center">
  <svg width="14" height="14" viewBox="0 0 24 24"><path d="M6.6 10.8a15 15 0 0 0 6.6 6.6l2.2-2.2a1 1 0 0 1 1-.25 11 11 0 0 0 3.6.6 1 1 0 0 1 1 1V20a1 1 0 0 1-1 1A17 17 0 0 1 3 4a1 1 0 0 1 1-1h3.5a1 1 0 0 1 1 1 11 11 0 0 0 .6 3.6 1 1 0 0 1-.25 1z" fill="#ff4f17"/></svg>
  (+1) 555 010 2040
</div>
<div class="abs foot-contact" style="left:838px;top:4236px;align-items:center">
  <svg width="14" height="12" viewBox="0 0 14 12"><rect width="14" height="12" rx="1" fill="#ff4f17"/><path d="M1 2l6 4 6-4" stroke="#1f2024" stroke-width="1.3" fill="none"/></svg>
  hello@apexreach.example
</div>
<div class="abs copyright">©APEX REACH - 2020 All rights reserved.</div>

</body>
</html>
```